Quiet Harbor Roasters - Full Brand Packaging Suite (Pods, Boxes, Bags)

Quiet Harbor Roasters is commissioning a complete packaging system for our 12‑roast specialty coffee collection. Each roast is inspired by a Christian ministry, and every package must follow a consistent storytelling structure across all formats: single‑serve pod lids, 12‑count and 24‑count pod boxes, 12 oz bags, and 2 lb bags.Packaging Formats Needed:• Single‑Serve Pod Lids: Circular design featuring roast name, roast type, ministry inspiration, and color theme.
• 12‑Count & 24‑Count Pod Boxes: Full panel design (front, back, sides, top) matching the roast’s identity and ministry story.
• 12 oz Bag: Vertical layout with strong shelf presence, roast color theme, ministry spotlight, and brand story.
• 2 lb Bag: Same design language as the 12 oz bag, scaled appropriately.
Required Panel Structure (applies to every roast):• Front Panel:• Roast Name
• Roast Type
• “Inspired By: [Ministry Name]”
• “Mission Driven | Fueling Global Impact”
• “Brew it. Share it. Fuel the Mission.”

• Side A — Roast Story:
A short, emotionally resonant description connecting the roast’s flavor profile or theme to the ministry’s impact.
• Side B — Ministry Spotlight:
Ministry name, mission summary, and a “Scan to Give” callout with website link.
• Back Panel:• Flavor Notes
• Origin
• Quiet Harbor Roasters Story (provided text stays consistent across all roasts)
• Statement of giving: “50% of net proceeds support our ministry partners + 10% of gross sales from each roast go directly to the ministry it represents.”

Brand Identity:
Quiet Harbor Roasters blends premium specialty coffee with faith‑driven purpose. Designs should feel clean, premium, unified, and visually distinct per roast through color, tone, and ministry theme.Deliverables:• Print‑ready files for all packaging formats
• Editable source files
• Cohesive color system across all 12 roasts
• Consistent layout structure across lids, boxes, and bags
Goal:
Create a unified, premium packaging system that elevates each roast’s identity, communicates its ministry partnership, and strengthens the mission‑driven heart of Quiet Harbor Roasters.

Target Market(s)

Churches

Industry/Entity Type

Churches, ministries, Christian’s

Requirements
Must have
• I’d like the design to look like the AI GENERATED image I had made of the packaging. It looks classy and clean.
Should not have
• Colorful palette, silly pictures, cartons, mascots

```html
<!DOCTYPE html>
<html lang="en">
<head>
<meta charset="utf-8">
<title>Quiet Harbor Roasters – Pod Lids &amp; Boxes</title>
<link rel="stylesheet" href="https://fonts.googleapis.com/css2?family=Oswald:wght@400;500;600&display=swap">
<style>
  :root {
    --canvas: #ffffff;
    --cream: #f3ebe1;
    --ink: #2b211b;
    --lid-edge: #9a9a9a;
    --sunrise: #d9952a;
    --meadow: #95b251;
    --harbor: #2e7e87;
    --on-accent: #ffffff;
  }
  * { box-sizing: border-box; margin: 0; padding: 0; }
  html, body { width: 1200px; height: 841px; overflow: hidden; background: var(--canvas); }
  body { font-family: "Oswald", "Arial Narrow", sans-serif; position: relative; text-transform: uppercase; }

  .roast-sunrise { --accent: var(--sunrise); }
  .roast-meadow  { --accent: var(--meadow); }
  .roast-harbor  { --accent: var(--harbor); }

  /* Brand name lockup */
  .brand-name {
    color: var(--ink);
    font-weight: 600;
    text-align: center;
    line-height: 0.95;
    letter-spacing: 0.5px;
  }

  /* Pod lids */
  .pod-lid {
    position: absolute;
    top: 67px;
    width: 187px;
    height: 187px;
    border-radius: 50%;
    border: 1px solid var(--lid-edge);
    overflow: hidden;
    background: var(--canvas);
  }
  .pod-lid .brand-name {
    position: absolute;
    top: 27px; left: 0; right: 0;
    font-size: 19px;
  }
  .pod-lid .lid-band {
    position: absolute;
    top: 93px; left: 0; right: 0; bottom: 0;
    background: var(--accent);
    color: var(--on-accent);
    text-align: center;
  }
  .lid-band .roast-icon { display: block; margin: 11px auto 0; width: 26px; height: 22px; }
  .lid-band .roast-name { font-size: 19px; font-weight: 500; line-height: 1.1; margin-top: 3px; }
  .lid-band .roast-type { font-size: 12px; font-weight: 400; line-height: 1.2; }

  /* Pod boxes */
  .pod-box {
    position: absolute;
    top: 334px;
    width: 343px;
    height: 439px;
    background: var(--cream);
    text-align: center;
  }
  .pod-box .brand-name {
    position: absolute;
    top: 70px; left: 0; right: 0;
    font-size: 25px;
  }
  .box-band {
    position: absolute;
    top: 172px; left: 0; right: 0;
    height: 166px;
    background: var(--accent);
    color: var(--on-accent);
  }
  .box-band .roast-name { font-size: 20px; font-weight: 500; margin-top: 10px; line-height: 1.1; }
  .box-band .roast-type { font-size: 12px; font-weight: 400; line-height: 1.2; }
  .box-band .roast-icon { display: block; width: 40px; height: 24px; margin: 13px auto 0; }
  .box-band .tagline { font-size: 12px; font-weight: 400; line-height: 1.25; margin-top: 8px; }
  .box-band .inspired { font-size: 7px; line-height: 1.4; margin-top: 9px; }
  .pod-count {
    position: absolute;
    top: 346px; left: 0; right: 0;
    color: var(--accent);
  }
  .pod-count .count { font-size: 12px; font-weight: 500; line-height: 1.1; }
  .pod-count .unit { font-size: 6.5px; margin-top: 1px; }

  .col-1 { left: 128px; }
  .col-2 { left: 508px; }
  .col-3 { left: 888px; }
  .box-1 { left: 50px; }
  .box-2 { left: 430px; }
  .box-3 { left: 809px; }
</style>
</head>
<body>

<!-- Pod lids -->
<div class="pod-lid roast-sunrise col-1">
  <p class="brand-name">Quiet Harbor<br>Roasters</p>
  <div class="lid-band">
    <svg class="roast-icon" viewBox="0 0 40 24" fill="none" stroke="#fff" stroke-width="1.2">
      <path d="M10 18a10 10 0 0 1 20 0"/><path d="M2 18h36"/><path d="M5 21h30"/>
      <path d="M20 2v4M10 5l2 3M30 5l-2 3M4 11l3 1.5M36 11l-3 1.5"/>
    </svg>
    <p class="roast-name">Morning Promise</p>
    <p class="roast-type">Breakfast Blend</p>
  </div>
</div>

<div class="pod-lid roast-meadow col-2">
  <p class="brand-name">Quiet Harbor<br>Roasters</p>
  <div class="lid-band">
    <svg class="roast-icon" viewBox="0 0 24 24" fill="none" stroke="#fff" stroke-width="1.3">
      <circle cx="12" cy="12" r="10"/><path d="M12 19v-7"/><path d="M12 13c-4 0-6-2-6-6 4 0 6 2 6 6z"/><path d="M12 12c0-4 2-6 6-6 0 4-2 6-6 6z"/>
    </svg>
    <p class="roast-name">Fields of Grace</p>
    <p class="roast-type">Light Roast</p>
  </div>
</div>

<div class="pod-lid roast-harbor col-3">
  <p class="brand-name">Quiet Harbor<br>Roasters</p>
  <div class="lid-band">
    <svg class="roast-icon" viewBox="0 0 24 24" fill="none" stroke="#fff" stroke-width="1.3">
      <path d="M12 3c3 4 5 7 5 9.5a5 5 0 0 1-10 0C7 10 9 7 12 3z"/><path d="M4 20c4 2 12 2 16 0"/>
    </svg>
    <p class="roast-name">Deep Wells</p>
    <p class="roast-type">Medium Roast</p>
  </div>
</div>

<!-- Pod boxes -->
<section class="pod-box roast-sunrise box-1">
  <p class="brand-name">Quiet Harbor<br>Roasters</p>
  <div class="box-band">
    <p class="roast-name">Morning Promise</p>
    <p class="roast-type">Breakfast Blend</p>
    <svg class="roast-icon" viewBox="0 0 40 24" fill="none" stroke="#fff" stroke-width="1">
      <path d="M10 18a10 10 0 0 1 20 0"/><path d="M2 18h36"/><path d="M5 21h30"/>
      <path d="M20 2v4M10 5l2 3M30 5l-2 3M4 11l3 1.5M36 11l-3 1.5"/>
    </svg>
    <p class="tagline">Mission Driven<br>Fueling Global Impact</p>
    <p class="inspired">Inspired by:<br>Bright Path Ministries</p>
  </div>
  <div class="pod-count"><p class="count">12</p><p class="unit">Single-serve pods</p></div>
</section>

<section class="pod-box roast-meadow box-2">
  <p class="brand-name">Quiet Harbor<br>Roasters</p>
  <div class="box-band">
    <p class="roast-name">Fields of Grace</p>
    <p class="roast-type">Light Roast</p>
    <svg class="roast-icon" viewBox="0 0 40 24" fill="none" stroke="#fff" stroke-width="1.2">
      <circle cx="20" cy="12" r="10"/><path d="M20 19v-7"/><path d="M20 13c-4 0-6-2-6-6 4 0 6 2 6 6z"/><path d="M20 12c0-4 2-6 6-6 0 4-2 6-6 6z"/>
    </svg>
    <p class="tagline">Brew it. Share it.<br>Fuel the mission.</p>
    <p class="inspired">Inspired by:<br>Open Field Relief</p>
  </div>
  <div class="pod-count"><p class="count">12</p><p class="unit">Single-serve pods</p></div>
</section>

<section class="pod-box roast-harbor box-3">
  <p class="brand-name">Quiet Harbor<br>Roasters</p>
  <div class="box-band">
    <p class="roast-name">Deep Wells</p>
    <p class="roast-type">Medium Roast</p>
    <svg class="roast-icon" viewBox="0 0 40 24" fill="none" stroke="#fff" stroke-width="1.2">
      <path d="M20 3c3 4 5 7 5 9.5a5 5 0 0 1-10 0C15 10 17 7 20 3z"/><path d="M12 20c4 2 12 2 16 0"/>
    </svg>
    <p class="tagline">Brew it. Share it.<br>Fuel the mission.</p>
    <p class="inspired">Inspired by:<br>Clear Spring Aid</p>
  </div>
  <div class="pod-count"><p class="count">12</p><p class="unit">Single-serve pods</p></div>
</section>

</body>
</html>
```